Sunridge Lighting Distributors Business Card Design

Use logo and expand the framing box to the extents of the business card. Keep company name in right bottom corner and triangle at top right corner. I would like to have a template so that I can fill in employee name, contact info, email and website.

```html
<!DOCTYPE html>
<html lang="en">
<head>
<meta charset="utf-8">
<title>Sunridge Lighting Distributors – Business Card</title>
<link rel="stylesheet" href="https://fonts.googleapis.com/css2?family=Quicksand:wght@500;700&display=swap">
<style>
  :root {
    --ink: #222222;
    --blue: #1e7fcb;
    --paper: #ffffff;
    --backdrop: #dcdde0;
    --text-grey: #3a3a3a;
  }
  * { margin: 0; padding: 0; box-sizing: border-box; }
  html, body { width: 1200px; height: 800px; overflow: hidden; }
  body {
    background: var(--backdrop);
    font-family: "Quicksand", sans-serif;
    position: relative;
  }
  .card {
    position: absolute;
    top: 245px;
    width: 540px;
    height: 309px;
    background: var(--paper);
    box-shadow: 0 6px 18px rgba(0,0,0,0.18);
    overflow: hidden;
  }
  .card--back { left: 40px; }
  .card--front { left: 620px; }
  .card__frame {
    position: absolute;
    inset: 12px;
    border: 18px solid var(--ink);
  }
  .card__corner {
    position: absolute;
    inset: 0;
    width: 540px;
    height: 309px;
  }
  .company-name {
    position: absolute;
    color: var(--ink);
    font-weight: 700;
    font-size: 26px;
    line-height: 1.05;
    text-transform: uppercase;
    letter-spacing: 0.5px;
  }
  .card--back .company-name { right: 70px; bottom: 58px; }
  .card--front .company-name { left: 62px; top: 104px; }
  .website-line {
    position: absolute;
    left: 58px;
    top: 58px;
    font-size: 13px;
    font-weight: 700;
    letter-spacing: 3px;
    color: var(--ink);
  }
  .website-line .domain { color: var(--blue); }
  .contact {
    position: absolute;
    right: 62px;
    top: 84px;
    text-align: right;
    color: var(--text-grey);
  }
  .contact__name {
    color: var(--blue);
    font-weight: 700;
    font-size: 15px;
    letter-spacing: 0.5px;
    text-transform: uppercase;
  }
  .contact__title {
    font-size: 12px;
    font-weight: 500;
    margin-bottom: 12px;
  }
  .contact__list { list-style: none; }
  .contact__item {
    display: flex;
    justify-content: flex-end;
    align-items: center;
    gap: 6px;
    font-size: 13px;
    font-weight: 500;
    line-height: 22px;
  }
  .contact__icon { width: 12px; height: 12px; fill: var(--blue); flex: none; }
</style>
</head>
<body>

  <section class="card card--back" aria-label="Card back">
    <div class="card__frame"></div>
    <svg class="card__corner" viewBox="0 0 540 309" aria-hidden="true">
      <polygon points="0,0 120,0 0,120" fill="#ffffff"/>
      <polygon points="0,0 100,0 0,100" fill="var(--blue)"/>
    </svg>
    <p class="website-line">www.<span class="domain">sunridgelighting</span>.com</p>
    <p class="company-name">Sunridge<br>Lighting<br>Distributors</p>
  </section>

  <section class="card card--front" aria-label="Card front">
    <div class="card__frame"></div>
    <svg class="card__corner" viewBox="0 0 540 309" aria-hidden="true">
      <polygon points="420,0 540,0 540,120" fill="#ffffff"/>
      <polygon points="440,0 540,0 540,100" fill="var(--blue)"/>
    </svg>
    <p class="company-name">Sunridge<br>Lighting<br>Distributors</p>
    <div class="contact">
      <p class="contact__name">Rowan Ellery</p>
      <p class="contact__title">Director</p>
      <ul class="contact__list">
        <li class="contact__item">555-0140-2210
          <svg class="contact__icon" viewBox="0 0 12 12" aria-hidden="true"><path d="M2.5 1 4.5 1 5.3 3.6 4 4.6a6.5 6.5 0 0 0 3.4 3.4l1-1.3L11 7.5v2L9.8 11C5 10.7 1.3 7 1 2.2Z"/></svg>
        </li>
        <li class="contact__item">info@sunridgelighting.com
          <svg class="contact__icon" viewBox="0 0 12 12" aria-hidden="true"><path d="M1 3h10v7H1Z M1 3l5 4 5-4" stroke="#fff" stroke-width="0.8"/></svg>
        </li>
        <li class="contact__item">www.sunridgelighting.com
          <svg class="contact__icon" viewBox="0 0 12 12" aria-hidden="true"><circle cx="6" cy="6" r="5"/><path d="M1 6h10M6 1c-2.5 3-2.5 7 0 10M6 1c2.5 3 2.5 7 0 10" stroke="#fff" stroke-width="0.8" fill="none"/></svg>
        </li>
        <li class="contact__item">00 dummy city, place 0000
          <svg class="contact__icon" viewBox="0 0 12 12" aria-hidden="true"><path d="M6 11.5C3.5 8.5 2 6.5 2 4.5a4 4 0 0 1 8 0c0 2-1.5 4-4 7Z"/><circle cx="6" cy="4.5" r="1.5" fill="#fff"/></svg>
        </li>
      </ul>
    </div>
  </section>

</body>
</html>
```